Guaranteed Job - Sleek Sexy Business Card UV Spot

Im looking for a sleek and sexy business card, that resembles elite or VIP status status.
our business is corinvale.example
you can view our products on there, but our main audience for handing out our cards will be for people in the hospitality industry, so it will need to impress high management and CEO of hotels and restaurants, bars, clubs etc...
the card features will have UV spot on both sides, 400gsm stock. standard size.
Artwork should be 86 x 54mm + 2mm bleed = 90 x 58mm
it should have a nice "unique" uv spot pattern that highlights the card, not a repeated pattern, theres no originality there, and it will be disregarded.
The written material will be:
Corin Vale Hospitality College (logo)
Tobin Marsh
Director
Phone: 1300 615 737
Mobile: 0455 817 296
Email: info@corinvale.example
website: www.corinvale.example
I'm looking for originality here, i don't want just a simple stock card, want something that has a wow factor for people.
You will find the logo attached. you may invert the white to black words to suit the background as you please.
thank you and good luck
As a side note, ive received a lot of proposals, im too busy to give feedback to each and every one, so if i havent provided feedback for your design within 24 hours, then consider it not acceptable, and you could resubmit another design.
So far i have not seen any design that stood out for me, they all seem pretty generic. there nothing thats unique, i would figure for the amount that im offering, that people would put some more effort and creativity into the design.
so far over 200 designs submitted, and nothing i have seen looks very original, everything looks like a different variation of the same stuff, i said it very clearly i wanted something unique, the only thing that has come close to it so far is this one
Reason: Ive received alot of design concepts and i have reviewed everyone, but i havent had time to give feedback to every single one, only the ones that have interested me, if i havent responded, its because i havent found it good enough.
so far only a few design have been on par with what ive been looking for, an attractive eye popping design.
heres a few of them,
http://files.pixelbazaar.example/design_img/51736/62418/62418_2840915_51736_image.jpg
http://files.pixelbazaar.example/design_img/51736/68254/68254_2841377_51736_image.jpg
theyre, both unique and original, and eye catching, the only thing theyre missing is the sexyness.
if you still think you have some creativity left in your minds, then throw it on here.
Reason: Sorry guys for the delay, I was in a serious accident and out of commission for the past few months, I'm just slowly recovering now, please bare with me as i try to attend to this project, it may take me awhile as I have other projects that are on standby, I'm not 100% at the moment, so im extending the deadline for 2 weeks right now. Thanks for your patience.
Hospitality

```html
<!DOCTYPE html>
<html lang="en">
<head>
<meta charset="utf-8">
<title>Corin Vale Hospitality College – Business Card</title>
<link rel="stylesheet" href="https://fonts.googleapis.com/css2?family=Barlow+Semi+Condensed:wght@400;500;600&display=swap">
<style>
  :root {
    --backdrop: #3a2a20;
    --card: #000000;
    --accent-blue: #5aaee0;
    --splash-soft: rgba(90, 174, 224, 0.0);
    --text-white: #ffffff;
    --ghost: rgba(255, 255, 255, 0.07);
    --card-shadow: 0 6px 14px rgba(0, 0, 0, 0.55);
  }
  * { box-sizing: border-box; margin: 0; padding: 0; }
  html, body {
    width: 1200px;
    height: 900px;
    overflow: hidden;
    background: var(--backdrop);
    font-family: "Barlow Semi Condensed", "Arial Narrow", sans-serif;
  }
  .stage { position: relative; width: 1200px; height: 900px; }
  .card {
    position: absolute;
    left: 113px;
    width: 550px;
    height: 348px;
    background: var(--card);
    box-shadow: var(--card-shadow);
    overflow: hidden;
  }
  .card--front { top: 72px; }
  .card--back { top: 447px; }

  .splash-area {
    position: absolute;
    left: 190px; top: 0;
    width: 360px; height: 348px;
    background: radial-gradient(ellipse 62% 58% at 58% 62%,
      var(--accent-blue) 0%, var(--accent-blue) 38%, var(--splash-soft) 100%);
  }

  .brand {
    position: absolute;
    left: 10px; top: 22px;
    display: flex;
    align-items: center;
    gap: 24px;
  }
  .brand__square {
    width: 72px; height: 72px;
    background: var(--accent-blue);
  }
  .brand__name {
    color: var(--text-white);
    font-weight: 500;
    line-height: 0.98;
    text-transform: uppercase;
  }
  .brand__line { display: block; font-size: 36px; letter-spacing: 0.3px; }
  .brand__line--small { font-size: 15px; letter-spacing: 0.8px; margin-top: 3px; }

  .person {
    position: absolute;
    left: 32px; top: 148px;
    color: var(--text-white);
  }
  .person__name {
    font-size: 29px;
    font-weight: 600;
    line-height: 1;
    text-transform: uppercase;
  }
  .person__first { color: var(--accent-blue); }
  .person__role {
    font-size: 21px;
    font-weight: 600;
    margin-top: 4px;
  }

  .contacts {
    position: absolute;
    left: 12px; top: 236px;
    list-style: none;
  }
  .contacts__item {
    display: flex;
    align-items: center;
    gap: 12px;
    height: 25px;
    color: var(--text-white);
    font-size: 17px;
    font-weight: 600;
  }
  .contacts__icon { width: 21px; height: 21px; flex: none; }
  .contacts__icon circle { fill: none; stroke: var(--text-white); stroke-width: 1.6; }
  .contacts__icon .glyph { fill: var(--text-white); }
  .contacts__icon .glyph-line { fill: none; stroke: var(--text-white); stroke-width: 1.2; }

  .ghost-name {
    position: absolute;
    left: 28px; top: 70px;
    color: var(--ghost);
    font-weight: 500;
    font-size: 120px;
    line-height: 0.95;
    text-transform: uppercase;
  }
</style>
</head>
<body>
<main class="stage">

  <section class="card card--front" aria-label="Business card front">
    <div class="splash-area" role="img" aria-label="Blue cocktail splash illustration"></div>

    <div class="brand">
      <span class="brand__square" aria-hidden="true"></span>
      <p class="brand__name">
        <span class="brand__line">Corin</span>
        <span class="brand__line">Vale</span>
        <span class="brand__line brand__line--small">Hospitality College</span>
      </p>
    </div>

    <div class="person">
      <h1 class="person__name"><span class="person__first">Tobin</span> Marsh</h1>
      <p class="person__role">Director</p>
    </div>

    <ul class="contacts">
      <li class="contacts__item">
        <svg class="contacts__icon" viewBox="0 0 22 22" aria-hidden="true"><circle cx="11" cy="11" r="9.5"/><path class="glyph" d="M7.5 6.5l2-0.5 1 2.5-1.2 1c.6 1.4 1.6 2.4 3 3l1-1.2 2.5 1-.5 2c-4 .3-8-3.7-7.8-7.8z"/></svg>
        1300 615 737
      </li>
      <li class="contacts__item">
        <svg class="contacts__icon" viewBox="0 0 22 22" aria-hidden="true"><circle cx="11" cy="11" r="9.5"/><rect class="glyph" x="8" y="5.5" width="6" height="11" rx="1"/></svg>
        0455 817 296
      </li>
      <li class="contacts__item">
        <svg class="contacts__icon" viewBox="0 0 22 22" aria-hidden="true"><circle cx="11" cy="11" r="9.5"/><path class="glyph-line" d="M6 7.5h10v7H6z M6.8 8.2l4.2 3.3 4.2-3.3"/></svg>
        info@corinvale.example
      </li>
      <li class="contacts__item">
        <svg class="contacts__icon" viewBox="0 0 22 22" aria-hidden="true"><circle cx="11" cy="11" r="9.5"/><path class="glyph" d="M11 5.5l5.5 5h-1.5v5h-2.5v-3h-3v3h-2.5v-5h-1.5z"/></svg>
        www.corinvale.example
      </li>
    </ul>
  </section>

  <section class="card card--back" aria-label="Business card back">
    <div class="splash-area" role="img" aria-label="Blue cocktail splash illustration"></div>
    <p class="ghost-name" aria-hidden="true">Corin<br>Vale</p>
  </section>

</main>
</body>
</html>
```